Book Cover for: TITLE Mend the Quiet Hours SUBTITLE For couples who don't want to break up

We need a full cover design for a book on relationships written by husband and wife team, Marla and Walter Dunmore, PhD. This book will offer hope for couples that are on the verge of breaking up but want to work things out and stay together. The theme is to teach couples about their own reactions to their partner, how moods affect a relationship, how to get creative to solving problems and how to have a good feeling towards your partner regardless of differences. This book is about hope. It is a positive look at relationships that feel hopeless.

Target Market(s)

Married or couples that are going through a difficult time and are considering splitting up due to, communication difficulties, addiction, affair. We imagine the book will appeal to women more than men but still want a cover that men would be comfortable picking up.

Colors

Designer to choose colors to be used in the design.

Requirements
Must have
• We want the cover to beautiful, intriguing, simple and uncomplicated. We don't want it overly busy, technical, or complex.
Nice to have
• MAYBE?? a broken heart being put back together.
Should not have
• No photo, no cartoon, no flowers, no couple (unless obscure and not gender specific).

```html
<!DOCTYPE html>
<html lang="en">
<head>
<meta charset="utf-8">
<title>Mend the Quiet Hours — Book Cover</title>
<link href="https://fonts.googleapis.com/css2?family=Anton&family=Kaushan+Script&family=Josefin+Sans:wght@500&display=swap" rel="stylesheet">
<style>
  :root {
    --backdrop: #e4e4e6;
    --paper: #ffffff;
    --title-red: #a0121a;
    --script-red: #a3141b;
    --ink: #111111;
    --heart-red: #d8141c;
    --heart-deep: #b3131a;
    --heart-dark: #3a3a3d;
  }
  html, body {
    margin: 0;
    padding: 0;
    width: 886px;
    height: 1200px;
    overflow: hidden;
    background: var(--backdrop);
  }
  .cover {
    position: absolute;
    left: 43px;
    top: 0;
    width: 800px;
    height: 1200px;
    background: var(--paper);
    overflow: hidden;
  }
  .cover-title {
    position: absolute;
    top: 84px;
    left: 0;
    width: 100%;
    margin: 0;
    text-align: center;
    white-space: nowrap;
    font-family: "Anton", sans-serif;
    font-weight: 400;
    font-size: 74px;
    line-height: 1;
    letter-spacing: 0;
    text-transform: uppercase;
    color: var(--title-red);
    transform: scaleY(1.25);
    transform-origin: 50% 0;
  }
  .cover-art {
    position: absolute;
    left: 90px;
    top: 196px;
    width: 620px;
    height: 730px;
    background: radial-gradient(closest-side,
      var(--heart-red) 0%,
      var(--heart-deep) 40%,
      var(--heart-dark) 66%,
      rgba(216, 20, 28, 0.5) 82%,
      rgba(255, 255, 255, 0) 100%);
  }
  .cover-subtitle {
    position: absolute;
    top: 928px;
    left: 0;
    width: 100%;
    margin: 0;
    text-align: center;
    font-family: "Kaushan Script", cursive;
    font-weight: 400;
    font-size: 62px;
    line-height: 82px;
    color: var(--script-red);
  }
  .cover-subtitle .line { display: block; white-space: nowrap; }
  .cover-subtitle .line-first { margin-left: -20px; }
  .cover-credit {
    position: absolute;
    top: 1100px;
    left: 0;
    width: 100%;
    margin: 0;
    text-align: center;
    font-family: "Josefin Sans", sans-serif;
    font-weight: 500;
    text-transform: uppercase;
    color: var(--ink);
  }
  .credit-label {
    display: block;
    font-size: 28px;
    line-height: 34px;
    margin-left: 0;
  }
  .credit-names {
    display: block;
    font-size: 27px;
    line-height: 34px;
    margin-top: 4px;
    margin-left: 20px;
    white-space: nowrap;
  }
</style>
</head>
<body>
  <main class="cover">
    <h1 class="cover-title">Mend the Quiet Hours</h1>
    <div class="cover-art" role="img" aria-label="Illustration of an anatomical red heart, partly black and grey, wrapped in a thorny vine of red roses, set against red and black ink splatters with dripping paint"></div>
    <p class="cover-subtitle">
      <span class="line line-first">For couples who</span>
      <span class="line">don't want to break up</span>
    </p>
    <p class="cover-credit">
      <span class="credit-label">Author</span>
      <span class="credit-names">Marla and Walter Dunmore, PhD</span>
    </p>
  </main>
</body>
</html>
```